Torvik Apparel Brochure Project

Looking for a brochure to send out with samples of our apparel. The name of our company is Torvik Apparel and we are distributors for 7.42. I have attached an older 7.42 brochure. I would like the brochure to be regular paper size with no folds.

Target Market(s)

Buyers working for large U.S. retail stores

Colors

Designer to choose colors to be used in the design.

Requirements
Must have
• Must look sleek and professional.

```html
<!DOCTYPE html>
<html lang="en">
<head>
<meta charset="utf-8">
<title>Khadi</title>
<link rel="stylesheet" href="https://fonts.googleapis.com/css2?family=Marcellus+SC&family=Noto+Serif:wght@300;400&display=swap">
<style>
  :root {
    --paper: #ffffff;
    --ink: #2b2b2b;
    --rule: #9a9a9a;
    --accent: #a31f24;
    --photo-garden: #6d6a45;
    --photo-garden-light: #a9a47a;
    --photo-fence: #8a9a6a;
    --photo-fence-light: #c9cdb8;
  }
  html, body {
    margin: 0;
    padding: 0;
    overflow: hidden;
    background: var(--paper);
  }
  .page {
    position: relative;
    width: 848px;
    height: 1200px;
    background: var(--paper);
    color: var(--ink);
    overflow: hidden;
  }
  .page-title {
    position: absolute;
    top: 48px;
    left: 0;
    width: 848px;
    margin: 0;
    text-align: center;
    font-family: "Marcellus SC", serif;
    font-weight: 400;
    font-size: 40px;
    letter-spacing: 3px;
    line-height: 1;
    color: var(--ink);
  }
  .title-divider {
    position: absolute;
    top: 102px;
    left: 339px;
  }
  .photo {
    position: absolute;
    margin: 0;
  }
  .photo-dress {
    left: 83px;
    top: 155px;
    width: 346px;
    height: 448px;
    background: linear-gradient(160deg, var(--photo-garden-light), var(--photo-garden) 60%, #4d4a30);
  }
  .photo-top {
    left: 434px;
    top: 618px;
    width: 347px;
    height: 466px;
    background: linear-gradient(180deg, var(--photo-fence-light), var(--photo-fence) 55%, #4f6a3a 80%, #c9c3b6);
  }
  .body-copy {
    position: absolute;
    margin: 0;
    font-family: "Noto Serif", serif;
    font-weight: 300;
    font-size: 25px;
    line-height: 45.7px;
    color: var(--ink);
  }
  .copy-intro {
    left: 466px;
    top: 227px;
    width: 330px;
  }
  .copy-artisans {
    left: 84px;
    top: 655px;
    width: 330px;
  }
  .page-number {
    position: absolute;
    left: 755px;
    top: 1115px;
    width: 93px;
    height: 55px;
    background: var(--accent);
    color: #ffffff;
    font-family: "Marcellus SC", serif;
    font-size: 32px;
    line-height: 55px;
    text-align: center;
  }
</style>
</head>
<body>
  <main class="page">
    <h1 class="page-title">Khadi</h1>
    <svg class="title-divider" width="174" height="12" viewBox="0 0 174 12" aria-hidden="true">
      <line x1="1" y1="6" x2="77" y2="6" stroke="#9a9a9a" stroke-width="1.2"/>
      <line x1="97" y1="6" x2="173" y2="6" stroke="#9a9a9a" stroke-width="1.2"/>
      <rect x="84" y="3" width="5" height="5" fill="#b0b0b0" transform="rotate(45 86.5 5.5)"/>
    </svg>

    <div class="photo photo-dress" role="img" aria-label="Model in a white sleeveless khadi dress standing in a sunlit garden"></div>

    <p class="body-copy copy-intro">Khadi is an ideal choice for green and ethical clothing. Made from cotton, silk, wool and other natural fibers, these fabrics have been in existence for hundreds of years.</p>

    <p class="body-copy copy-artisans">Today the production of khadi provides sustenance to millions of people in India. About eighty percent of khadi artisans are women, often from some of the poorest communities in the country.</p>

    <div class="photo photo-top" role="img" aria-label="Model seen from behind wearing a white sleeveless khadi top beside a garden fence"></div>

    <div class="page-number">4</div>
  </main>
</body>
</html>
```